Family Farm Business Requires Flyer for local CSA retail sales and local advertising

We need a flyer design for our small farm to help promote our CSA business. A CSA is when someone pre-pays for a summer's worth of produce, fruit, and eggs that are raised on our farm. They receive a weekly box of produce and essentially they buy a small share of the summer's bounty. We had a logo designed by someone here on sketch harbor so we would like the flyer to include the colors of the logo. The final design should reflect the different options for people the choose and then invite them to sign up to be a CSA Customer.

Target Market(s)

Busy families and moms who are limited in time to buy groceries or healthy food or produce. People who are passionate about local food and local produce.

Industry/Entity Type

Advertising

Font styles to use
Decorative
Script

Requirements
Must have
• Our logo, our farm information (website, social media, location) and contact info as well as the various options to choose from for our CSA farm share. I also included a picture of our business card so it would be good if it matched the colors/style of our card. Also the flyer will be printed on 8.5 x 11 paper and it will be double sided.

```html
<!DOCTYPE html>
<html lang="en">
<head>
<meta charset="utf-8">
<title>Nine Hollow Farm – CSA Flyer</title>
<link href="https://fonts.googleapis.com/css2?family=Comfortaa:wght@700&family=Lato:wght@400;700&family=Yanone+Kaffeesatz:wght@600;700&display=swap" rel="stylesheet">
<style>
:root{
  --green-dark:#149a4a;
  --green-light:#8dc63f;
  --yellow:#fbbf0a;
  --black:#000;
  --white:#fff;
  --ink:#333;
  --field:#c8c8c8;
  --field-alt:#dcdcdc;
  --page:#e9e6e1;
}
*{margin:0;padding:0;box-sizing:border-box}
html,body{width:806px;height:1200px;overflow:hidden;background:var(--page)}
.flyer{position:absolute;left:42px;top:105px;width:718px;height:985px;background:var(--white);overflow:hidden;font-family:'Lato',sans-serif;color:var(--ink);box-shadow:0 4px 14px rgba(0,0,0,.25)}
.flyer-shapes{position:absolute;inset:0}
.produce-photo{position:absolute;left:278px;top:40px;width:440px;height:290px;background:radial-gradient(ellipse at 60% 55%,#c8352a 0%,#e98a1f 30%,#8fbf3a 55%,#1a1a1a 80%)}
.brand{position:absolute;left:34px;top:60px;width:240px;color:var(--white)}
.brand-mark{display:block;width:46px;height:46px;border-radius:50%;background:var(--yellow);margin-bottom:14px}
.brand-name{font-family:'Lato',sans-serif;font-weight:700;font-size:44px;line-height:1.05;letter-spacing:3px;color:var(--white);text-transform:uppercase}
.brand-place{font-weight:700;font-size:20px;letter-spacing:2px;margin-top:14px;color:var(--white)}
.basket-photo{position:absolute;left:34px;top:423px;width:280px;height:181px;border:7px solid var(--green-light);border-radius:18px;background:radial-gradient(ellipse at 50% 55%,#c9a63a 0%,#b53a2a 30%,#6d4a25 55%,#0c0c0c 80%)}
.headline{position:absolute;left:336px;top:436px;font-family:'Comfortaa',sans-serif;font-weight:700;line-height:1}
.headline-fresh{display:block;font-size:70px;color:var(--green-light);letter-spacing:1px}
.headline-local{display:block;font-size:70px;color:var(--yellow);margin-top:4px;letter-spacing:1px}
.headline-tag{position:absolute;left:650px;top:582px;transform:rotate(-90deg);transform-origin:left top;font-family:'Yanone Kaffeesatz',sans-serif;font-weight:700;font-size:30px;color:var(--green-dark);letter-spacing:1px}
.signup-title{position:absolute;left:336px;top:605px;font-size:22px;color:#444}
.signup-form{position:absolute;left:336px;top:642px;width:352px;list-style:none}
.signup-form li{height:20px;margin-bottom:7.5px;background:linear-gradient(90deg,var(--field),var(--field-alt));font-size:13px;color:#444;padding:2px 4px}
.options{position:absolute;left:32px;top:626px;width:300px}
.options-title{font-family:'Yanone Kaffeesatz',sans-serif;font-weight:700;font-size:28px;color:var(--green-dark);line-height:1}
.options-title span{color:var(--green-light)}
.options-note{font-weight:700;font-size:12.5px;color:var(--green-light);line-height:1.25;margin:6px 0 10px}
.options-list{list-style:none;font-size:12.5px;line-height:1.45;color:#444}
.options-list li{position:relative;padding-left:14px}
.options-list li::before{content:"";position:absolute;left:0;top:5px;width:8px;height:8px;background:var(--green-light)}
.options-list .price{color:var(--green-dark);font-weight:700}
.footer-address,.footer-contact{position:absolute;color:var(--white);font-weight:700;font-size:19px;line-height:1.35}
.footer-address{left:34px;top:908px}
.footer-address .line{display:flex;align-items:center;gap:8px}
.footer-address .indent{padding-left:28px}
.footer-contact{right:30px;top:904px;text-align:right}
.footer-contact .line{display:flex;align-items:center;justify-content:flex-end;gap:8px;margin-bottom:4px}
.icon{width:20px;height:18px;flex:none}
</style>
</head>
<body>
<main class="flyer">
  <svg class="flyer-shapes" width="718" height="985" viewBox="0 0 718 985" aria-hidden="true">
    <rect class="header-bg" x="0" y="0" width="718" height="340" fill="var(--black)"/>
    <path d="M0 300 L343 378 L718 290 L718 330 L343 410 L0 336 Z" fill="var(--green-dark)"/>
  </svg>
  <div class="produce-photo" role="img" aria-label="Basket of fresh fruit: apples, grapes, bananas, oranges, melon and pineapple on black"></div>
  <svg class="flyer-shapes" width="718" height="985" viewBox="0 0 718 985" aria-hidden="true">
    <path d="M0 318 L343 392 L718 306 L718 325 L343 410 L0 336 Z" fill="var(--green-light)"/>
    <path d="M0 336 L343 410 L718 325 L718 340 L343 418 L0 350 Z" fill="var(--green-dark)"/>
    <path d="M0 350 L343 418 L718 340 L718 985 L0 985 Z" fill="#f7f7f7"/>
    <path d="M0 832 L343 900 L718 828 L718 985 L0 985 Z" fill="var(--green-light)"/>
    <path d="M0 846 L343 914 L718 842 L718 985 L0 985 Z" fill="var(--green-dark)"/>
  </svg>

  <header class="brand">
    <span class="brand-mark" aria-hidden="true"></span>
    <h1 class="brand-name">Nine<br>Hollow<br>Farm</h1>
    <p class="brand-place">MILLBROOK, VA</p>
  </header>

  <div class="basket-photo" role="img" aria-label="Woven basket of apples and lemons on black"></div>

  <h2 class="headline"><span class="headline-fresh">FRESH</span><span class="headline-local">LOCAL</span></h2>
  <span class="headline-tag">SUSTAINABLE</span>

  <section class="options">
    <h3 class="options-title">Options: <span>(Please Check)</span></h3>
    <p class="options-note">Summer CSA (18 weeks – weekly delivery starting June 1st through October 11th)</p>
    <ul class="options-list">
      <li>Mini Share (1 to 2 people) <span class="price">$325.00</span></li>
      <li>Standard Share ( 4 to 6 people) <span class="price">$425.00</span></li>
      <li>Family Share $500.00 (6 to 8 people)</li>
      <li>Fruit Share Add-on <span class="price">$50 to $75</span> depending on size (please indicate when ordering)</li>
      <li>Egg Share Add-on <span class="price">$90</span></li>
    </ul>
  </section>

  <h3 class="signup-title">2015 CSA Membership Sign –Up</h3>
  <ul class="signup-form">
    <li>Name</li><li>Address</li><li>State</li><li>ZIP Code</li>
    <li>Telephone (home)</li><li>Telephone (cell)</li><li>E-Mail</li>
  </ul>

  <address class="footer-address" style="font-style:normal">
    <span class="line"><svg class="icon" viewBox="0 0 20 18" aria-hidden="true"><path d="M2 9 L10 2 L18 9 M4 8 V16 H16 V8 M8 16 V11 H12 V16" fill="none" stroke="#fff" stroke-width="1.8"/></svg>1200 Orchard Lane Road</span>
    <span class="line indent">Millbrook, Virginia</span>
  </address>
  <div class="footer-contact">
    <span class="line"><svg class="icon" viewBox="0 0 20 18" aria-hidden="true"><rect x="1" y="0" width="18" height="18" rx="3" fill="var(--green-light)"/><path d="M6 4 L8 4 L9 7 L7.5 8 Q9 11 11 12 L12 10.5 L15 11.5 L15 13.5 Q10 15 5 7 Z" fill="#fff"/></svg>1 555-014-2286</span>
    <span class="line"><svg class="icon" viewBox="0 0 20 18" aria-hidden="true"><rect x="1" y="3" width="18" height="12" fill="var(--green-light)"/><path d="M1 3 L10 10 L19 3" fill="none" stroke="#fff" stroke-width="1.5"/></svg>www.ninehollowfarm.com</span>
  </div>
</main>
</body>
</html>
```